Business Card Design

Please use the Logo for colors and styles, and create a business card using the following info:

Matthias Loeber
Web Developer

Loeber Solutions
+41 76 482 17 05
matthias@loeber-solutions.example
www.loeber-solutions.example

Download the logo at http://loeber-solutions.example/tl_files/loeber_solutions.zip

Thanks for your works!

```html
<!DOCTYPE html>
<html lang="en">
<head>
<meta charset="utf-8">
<title>Loeber Solutions – Business Card</title>
<link rel="stylesheet" href="https://fonts.googleapis.com/css2?family=Questrial&display=swap">
<style>
  :root {
    --page: #ffffff;
    --navy: #0a3a94;
    --sky: #2a8ef0;
    --blue-deep: #063d9c;
    --blue-mid: #1a6fe0;
    --blue-bright: #3198ff;
    --white: #ffffff;
  }
  * { margin: 0; padding: 0; box-sizing: border-box; }
  html, body {
    width: 1200px;
    height: 900px;
    overflow: hidden;
    background: var(--page);
    font-family: "Questrial", "Century Gothic", sans-serif;
  }
  .canvas {
    position: relative;
    width: 1200px;
    height: 900px;
  }
  .card {
    position: absolute;
    left: 327px;
    width: 623px;
    height: 381px;
    overflow: hidden;
  }
  .card--front {
    top: 42px;
    background: linear-gradient(180deg,
      var(--blue-deep) 0%,
      var(--blue-mid) 25%,
      var(--blue-bright) 50%,
      var(--blue-mid) 78%,
      var(--blue-deep) 100%);
    display: flex;
    align-items: center;
    justify-content: center;
  }
  .wordmark {
    color: var(--white);
    font-size: 55px;
    letter-spacing: 0;
    line-height: 1;
    white-space: nowrap;
    margin-top: -12px;
  }
  .card--back {
    top: 483px;
    background: var(--page);
  }
  .card__band {
    position: absolute;
    left: 0;
    top: 0;
    width: 224px;
    height: 100%;
    background: linear-gradient(90deg,
      #1f72e4 0%,
      var(--blue-bright) 20%,
      #1f72e4 45%,
      #0c4cb8 75%,
      var(--blue-deep) 100%);
  }
  .contact {
    position: absolute;
    left: 239px;
    top: 0;
    width: 384px;
    height: 100%;
    color: var(--navy);
    white-space: nowrap;
  }
  .contact > * {
    position: absolute;
    left: 0;
    line-height: 36px;
  }
  .contact__name {
    top: 50px;
    font-size: 28px;
    font-weight: 400;
  }
  .contact__role {
    top: 87px;
    font-size: 28px;
    color: var(--sky);
  }
  .contact__phone { top: 166px; font-size: 21px; }
  .contact__email { top: 205px; font-size: 18px; }
  .contact__web   { top: 243px; font-size: 18px; }
  .contact__brand {
    top: 303px;
    font-size: 22px;
    letter-spacing: 0.3px;
  }
</style>
</head>
<body>
  <main class="canvas">
    <section class="card card--front">
      <div class="wordmark">LOEBER SOLUTIONS</div>
    </section>

    <section class="card card--back">
      <div class="card__band" role="img" aria-label="Blue gradient band with faint hexagon texture"></div>
      <div class="contact">
        <h1 class="contact__name">Matthias Loeber</h1>
        <p class="contact__role">Web Developer</p>
        <p class="contact__phone">+41 76 482 17 05</p>
        <p class="contact__email">matthias@loeber-solutions.example</p>
        <p class="contact__web">www.loeber-solutions.example</p>
        <p class="contact__brand">LOEBER SOLUTIONS</p>
      </div>
    </section>
  </main>
</body>
</html>
```